Business Card Design Project

Basic business card with minimal details. I just need company name, email & web address, telephone and my name.
I would like the back of the card to be grey with my logo & company name centred.

Target Market(s)

Architects
Builders
Property Developers

Industry/Entity Type

Business

Font styles to use
Sans Serif

Colors

Designer to choose colors to be used in the design.

Requirements
Must have
• Framewise Build
Marcus Helby - Director
M: 0427 593184
E: marcus@framewisebuild.com.au
W: www.framewisebuild.com.au
Should not have
• No other images or pictures

```html
<!DOCTYPE html>
<html lang="en">
<head>
<meta charset="utf-8">
<title>Framewise Build – Business Card</title>
<link rel="stylesheet" href="https://fonts.googleapis.com/css2?family=Open+Sans:wght@400;600;700&display=swap">
<style>
  :root {
    --backdrop: #eceef0;
    --card-white: #fbfbfb;
    --slate: #4a5866;
    --brand-red: #a3162e;
    --strip-grey: #c4c4c4;
    --text-white: #ffffff;
  }
  * { margin: 0; padding: 0; box-sizing: border-box; }
  html, body {
    width: 1200px;
    height: 864px;
    overflow: hidden;
    background: var(--backdrop);
    font-family: "Open Sans", sans-serif;
  }
  .card {
    position: absolute;
    left: 100px;
    top: 146px;
    width: 1000px;
    height: 572px;
    background: var(--card-white);
    overflow: hidden;
    box-shadow: 0 10px 30px rgba(0,0,0,0.12);
  }
  .brand {
    position: absolute;
    left: 92px;
    top: 82px;
    display: flex;
    align-items: center;
    gap: 28px;
  }
  .brand-square {
    width: 92px;
    height: 92px;
    background: var(--brand-red);
  }
  .brand-name {
    font-size: 66px;
    font-weight: 600;
    color: var(--slate);
    letter-spacing: 1px;
    text-transform: uppercase;
    line-height: 1;
  }
  .rule-right {
    position: absolute;
    left: 840px;
    top: 168px;
    width: 160px;
    height: 4px;
    background: var(--slate);
  }
  .rule-left {
    position: absolute;
    left: 0;
    top: 246px;
    width: 520px;
    height: 4px;
    background: var(--slate);
  }
  .person {
    position: absolute;
    right: 180px;
    top: 176px;
    text-align: right;
  }
  .person-name {
    font-size: 32px;
    font-weight: 700;
    color: var(--brand-red);
    letter-spacing: 1px;
    text-transform: uppercase;
    line-height: 1.1;
  }
  .person-role {
    font-size: 18px;
    color: var(--slate);
  }
  .web-band {
    position: absolute;
    left: 540px;
    top: 252px;
    width: 460px;
    height: 46px;
    background: var(--slate);
    color: var(--text-white);
    font-size: 19px;
    display: flex;
    align-items: center;
    justify-content: flex-end;
    padding-right: 80px;
  }
  .phone-strip {
    position: absolute;
    left: 0;
    top: 298px;
    width: 540px;
    height: 46px;
    background: var(--strip-grey);
  }
  .phone-number {
    position: absolute;
    left: 120px;
    top: 258px;
    font-size: 22px;
    color: var(--brand-red);
    letter-spacing: 0.5px;
  }
  .contact-panel {
    position: absolute;
    left: 0;
    top: 344px;
    width: 1000px;
    height: 228px;
    background: var(--brand-red);
  }
  .contact-panel-top {
    position: absolute;
    left: 540px;
    top: 298px;
    width: 460px;
    height: 46px;
    background: var(--brand-red);
  }
  .contact-list {
    position: absolute;
    left: 120px;
    top: 392px;
    list-style: none;
    color: var(--text-white);
    font-size: 20px;
    line-height: 36px;
  }
  .contact-item {
    display: flex;
    align-items: center;
    gap: 14px;
  }
  .contact-item svg { width: 24px; height: 20px; flex: none; }
  .contact-item.plain { padding-left: 0; }
</style>
</head>
<body>
  <div class="card">
    <div class="brand">
      <div class="brand-square"></div>
      <div class="brand-name">Framewise Build</div>
    </div>

    <div class="rule-right"></div>
    <div class="rule-left"></div>

    <div class="person">
      <div class="person-name">Marcus Helby</div>
      <div class="person-role">Director</div>
    </div>

    <div class="web-band">www.framewisebuild.com.au</div>

    <div class="phone-strip"></div>
    <div class="phone-number">0427 593184</div>

    <div class="contact-panel-top"></div>
    <div class="contact-panel"></div>

    <ul class="contact-list">
      <li class="contact-item">
        <svg viewBox="0 0 24 20" aria-label="Fax">
          <rect x="6" y="1" width="12" height="5" fill="#fff"/>
          <rect x="1" y="7" width="22" height="8" rx="1.5" fill="#fff"/>
          <rect x="6" y="13" width="12" height="6" fill="#fff" stroke="#a3162e" stroke-width="1.5"/>
        </svg>
        <span>0000 000 000</span>
      </li>
      <li class="contact-item">
        <svg viewBox="0 0 24 20" aria-label="Email">
          <rect x="1" y="3" width="22" height="15" fill="#fff"/>
          <path d="M1 3 L12 12 L23 3 M1 18 L9 10 M23 18 L15 10" fill="none" stroke="#a3162e" stroke-width="1.5"/>
        </svg>
        <span>marcus@framewisebuild.com.au</span>
      </li>
      <li class="contact-item plain">
        <span>Your Address Inc 2nd Lane Ave Carlton, VIC 3053</span>
      </li>
    </ul>
  </div>
</body>
</html>
```